Executive Business Consulting for Telco Companies and Telco Start up companies

1.) Looking for an appealing and action oriented business card design.
2.)The target companies to work with start-ups and existing companies that focus on Business to Business applications
3.) For "VORANT", a Belgium based Executive consultancy company specialised in global reach starting from the centre of Europe = Brussels.
4.) Our core competence is the Go To Market in All major global regions, incl North America, Latin America, Asia, Japan, Europe and Africa.
5.) Design should be appealing to CEO, CFO and Venture Funds signalling; Expertise, Stability, Maturity and Commitment
6.) Preferred color scheme is Blue focussed and using a modern FONT.
7.) Logo design is included (uploaded)

Target Market(s)

Telecommunication Market. Companies in a B2B business model, developping services or applications to make business run more profitable

Industry/Entity Type

Business

Contact Information for Business Card

Company Name: VORANT
Name: Joris Vandelay
Titel: Managing Director
Address: Kalkweg 58 , B-9170 Meerdonk , Belgium
Tel: + 32 471 208 364
Email: joris_vandelay@plimbox.example
LinkedIn: be.netprofilo.example/in/jorisvandelay/

Font styles to use
Serif

Colors
0455a3
3277b5

Requirements
Must have
• Second Side Text: Execute Sales Strategy and Transformation

```html
<!DOCTYPE html>
<html lang="en">
<head>
<meta charset="utf-8">
<title>VORANT – Business Card</title>
<link rel="stylesheet" href="https://fonts.googleapis.com/css2?family=Exo+2:wght@400;500;800&display=swap">
<style>
  :root {
    --page: #e6e8eb;
    --card-top: #ffffff;
    --card-bottom: #e9eaec;
    --navy: #10336a;
    --blue: #0455a3;
    --blue-light: #3277b5;
    --grey-band: #8b8c8e;
    --ink: #2d2f33;
    --ink-soft: #4a4d52;
  }
  * { margin: 0; padding: 0; box-sizing: border-box; }
  html, body {
    width: 1200px; height: 900px; overflow: hidden;
    background: var(--page);
    font-family: "Exo 2", "Segoe UI", sans-serif;
  }
  .stage {
    width: 1200px; height: 900px;
    display: flex; align-items: center; justify-content: center;
  }
  .card {
    position: relative;
    width: 960px; height: 540px;
    border-radius: 44px;
    overflow: hidden;
    background: radial-gradient(ellipse at 45% 35%, var(--card-top) 0%, var(--card-bottom) 85%);
    box-shadow: 0 10px 30px rgba(0,0,0,.18);
  }
  .card__band {
    position: absolute; left: 0; right: 0; bottom: 0; height: 120px;
    background: linear-gradient(90deg, var(--grey-band) 0%, var(--blue) 55%, var(--blue-light) 100%);
  }

  .brand {
    position: absolute; left: 70px; top: 100px;
    display: flex; flex-direction: column; align-items: flex-start; gap: 22px;
  }
  .brand__dot {
    width: 120px; height: 120px; border-radius: 50%;
    background: var(--navy);
    margin-left: 20px;
  }
  .brand__name {
    font-weight: 800; font-size: 92px; line-height: 1;
    color: var(--navy); letter-spacing: 2px;
  }

  .contact {
    position: absolute; right: 60px; top: 46px;
    text-align: right; color: var(--ink);
  }
  .contact__name { font-size: 30px; font-weight: 500; letter-spacing: 2px; text-transform: uppercase; }
  .contact__title { font-size: 21px; color: var(--ink-soft); margin-top: 2px; }
  .contact__address { font-size: 21px; margin-top: 22px; line-height: 1.3; letter-spacing: .5px; }
  .contact__lines { list-style: none; margin-top: 20px; font-size: 16px; letter-spacing: .8px; }
  .contact__lines li {
    display: flex; justify-content: flex-end; align-items: center; gap: 8px;
    height: 27px;
  }
  .contact__lines svg { width: 16px; height: 16px; fill: var(--ink); flex: none; }
</style>
</head>
<body>
<main class="stage">
  <section class="card" aria-label="VORANT business card">
    <div class="card__band" role="img" aria-label="Decorative grey and blue band along the bottom of the card"></div>

    <div class="brand">
      <span class="brand__dot"></span>
      <span class="brand__name">VORANT</span>
    </div>

    <div class="contact">
      <p class="contact__name">Joris Vandelay</p>
      <p class="contact__title">Managing Director</p>
      <p class="contact__address">Lindeveld 12<br>B-9990 Brelmonde</p>
      <ul class="contact__lines">
        <li>+ 32 000 55 01 01
          <svg viewBox="0 0 24 24"><path d="M6.6 10.8a15.1 15.1 0 0 0 6.6 6.6l2.2-2.2c.3-.3.7-.4 1-.2 1.1.4 2.3.6 3.6.6.6 0 1 .4 1 1V20c0 .6-.4 1-1 1A17 17 0 0 1 3 4c0-.6.4-1 1-1h3.5c.6 0 1 .4 1 1 0 1.3.2 2.5.6 3.6.1.3 0 .7-.2 1z"/></svg></li>
        <li>+ 32 000 55 01 02
          <svg viewBox="0 0 24 24"><path d="M7 1h10a2 2 0 0 1 2 2v18a2 2 0 0 1-2 2H7a2 2 0 0 1-2-2V3a2 2 0 0 1 2-2zm0 3v15h10V4z"/></svg></li>
        <li>+ 32 000 55 01 03
          <svg viewBox="0 0 24 24"><path d="M7 2h9l3 3v5h1a2 2 0 0 1 2 2v8a2 2 0 0 1-2 2H4a2 2 0 0 1-2-2v-8a2 2 0 0 1 2-2h3zm2 2v6h8V6h-2V4zM6 14v2h3v-2zm5 0v2h3v-2zm5 0v2h3v-2z"/></svg></li>
        <li>joris_vandelay@plimbox.example
          <svg viewBox="0 0 24 24"><path d="M2 5h20v14H2zm2 2v.5l8 5 8-5V7zm0 2.8V17h16V9.8l-8 5z"/></svg></li>
        <li>be.netprofilo.example/in/jorisvandelay/
          <svg viewBox="0 0 24 24"><path d="M12 2a10 10 0 1 0 0 20 10 10 0 0 0 0-20zm0 2a8 8 0 0 1 0 16 8 8 0 0 1 0-16zm-1 2v12h2V6zM5 11v2h14v-2z"/></svg></li>
      </ul>
    </div>
  </section>
</main>
</body>
</html>
```